Business Card Design Project

Company Name - Kestrova Care

Wellness consulting and training company. Run through a medical centre.

Main colour themes are orange and blue, as in the logo. Want to replicate same effect with business cards.

To give a sense of freedom and potential as per the company name.

Want the business card to be in line with stationary design, which I have launched as well.

Double sided with design and colour on one side and details on other side.
Updates

Reason: Need business card and stationary design to be teed up.

Target Market(s)

35 to 65 age group.
New age and trendy

Industry/Entity Type

Training

Requirements
Must have
• Colours orange and blue as per logo
Nice to have
• Design to be similar to stationary design, letterhead and envelopes

```html
<!DOCTYPE html>
<html lang="en">
<head>
<meta charset="utf-8">
<title>Kestrova Care – Business Card</title>
<link href="https://fonts.googleapis.com/css2?family=Ubuntu:wght@300;400&display=swap" rel="stylesheet">
<style>
  :root {
    --brand-blue: #1a5cb4;
    --brand-orange: #f07a22;
    --card-white: #f6f7f8;
    --text-white: #ffffff;
    --backdrop: #e4e5e7;
  }
  * { box-sizing: border-box; margin: 0; padding: 0; }
  html, body { width: 1200px; height: 900px; overflow: hidden; }
  body {
    background: var(--backdrop);
    font-family: "Ubuntu", Arial, sans-serif;
    position: relative;
  }
  .card {
    position: absolute;
    width: 640px;
    height: 366px;
    overflow: hidden;
    box-shadow: 0 6px 18px rgba(0,0,0,0.18);
  }

  /* Front side */
  .card-front {
    left: 90px;
    top: 70px;
    background: var(--brand-orange);
    border-radius: 0 0 0 22px;
  }
  .card-front .top-band {
    position: absolute; left: 0; top: 0; right: 0; height: 18px;
    background: var(--brand-blue);
  }
  .card-front .front-panel {
    position: absolute; left: 24px; top: 18px; right: 0; bottom: 30px;
    background: linear-gradient(160deg, #ffffff 0%, var(--card-white) 70%, #e9ebee 100%);
    border-radius: 0 0 26px 30px;
  }
  .brand-lockup {
    position: absolute;
    display: flex;
    align-items: center;
    gap: 14px;
    color: var(--brand-blue);
    font-weight: 400;
    white-space: nowrap;
  }
  .brand-lockup .brand-dot {
    border-radius: 50%;
    background: var(--brand-orange);
    flex: none;
  }
  .card-front .brand-lockup {
    left: 150px; bottom: 78px;
    font-size: 62px;
    letter-spacing: -1px;
  }
  .card-front .brand-lockup .brand-dot { width: 40px; height: 40px; }

  /* Back side */
  .card-back {
    left: 470px;
    top: 470px;
    background: var(--card-white);
  }
  .card-back .top-band {
    position: absolute; left: 0; top: 0; right: 0; height: 18px;
    background: var(--brand-blue);
    z-index: 2;
  }
  .card-back .details-panel {
    position: absolute; inset: 0;
  }
  .card-back .brand-lockup {
    left: 44px; top: 168px;
    font-size: 34px;
    gap: 10px;
  }
  .card-back .brand-lockup .brand-dot { width: 22px; height: 22px; }
  .contact {
    position: absolute;
    left: 346px; top: 36px;
    color: var(--text-white);
    font-weight: 300;
  }
  .contact .person-name {
    color: var(--brand-blue);
    font-size: 26px;
    font-weight: 400;
  }
  .contact .person-role { font-size: 14px; margin-top: 4px; }
  .contact .address {
    font-size: 16px; line-height: 1.35;
    margin: 24px 0 0 18px;
    font-style: normal;
  }
  .contact .lines {
    list-style: none;
    font-size: 16px; line-height: 1.35;
    margin: 34px 0 0 28px;
  }
  .contact .lines .label { color: var(--brand-blue); margin-right: 4px; }
</style>
</head>
<body>
  <section class="card card-front" aria-label="Business card front">
    <div class="top-band"></div>
    <div class="front-panel"></div>
    <div class="brand-lockup">
      <span class="brand-dot"></span>
      <span class="brand-name">Kestrova Care</span>
    </div>
  </section>

  <section class="card card-back" aria-label="Business card back">
    <svg class="details-panel" viewBox="0 0 640 366" width="640" height="366" aria-hidden="true">
      <defs>
        <linearGradient id="whiteSide" x1="0" y1="0" x2="1" y2="1">
          <stop offset="0" stop-color="#e9ebee"/>
          <stop offset="0.5" stop-color="#ffffff"/>
          <stop offset="1" stop-color="#eceef0"/>
        </linearGradient>
      </defs>
      <rect x="0" y="0" width="640" height="366" fill="url(#whiteSide)"/>
      <polygon points="336,18 640,18 640,366 322,366" fill="var(--brand-orange)"/>
      <rect x="0" y="348" width="322" height="18" fill="var(--brand-orange)"/>
      <rect x="0" y="18" width="14" height="348" fill="var(--brand-orange)"/>
    </svg>
    <div class="top-band"></div>
    <div class="brand-lockup">
      <span class="brand-dot"></span>
      <span class="brand-name">Kestrova Care</span>
    </div>
    <div class="contact">
      <p class="person-name">Marek Ellory</p>
      <p class="person-role">Chief Executive Officer</p>
      <address class="address">18 Halden Lane<br>Brookvale, NSW 2100</address>
      <ul class="lines">
        <li><span class="label">T:</span>555.204.3187</li>
        <li><span class="label">F:</span>555.204.3187</li>
        <li><span class="label">E:</span>info@kestrovacare.com</li>
        <li><span class="label">W:</span>www.KestrovaCare.com</li>
      </ul>
    </div>
  </section>
</body>
</html>
```